Business card design for an Art Director working for museums

The business card design we're looking for is for an Art Director in a private museum called "OLV Gallery". The museum showcases artworks made by the country's national artists. Designs should use the CMYK "0 40 100 20". You have the liberty to use any type you want except for overly decorative ones.

Target Market(s)

Professional and creative individuals. Interior designers, museum curators, museum coordinators etc

Industry/Entity Type

Museum

Contact Information for Business Card

Rel T
Art Director
+1 555 374 9281

Font styles to use
Serif
Sans Serif
Script

Requirements
Must have
• My project must have the CMYK 0 40 100 20. You can play with the Key.
• We're keen on clean, minimal, and architectural-type design.
Nice to have
• Geometric gradients that nicely complement the main CMYK that we've posted.
Should not have
• Off-putting colour palettes

```html
<!DOCTYPE html>
<html lang="en">
<head>
<meta charset="utf-8">
<title>OLV Gallery — Business Card</title>
<link href="https://fonts.googleapis.com/css2?family=PT+Sans:ital,wght@0,400;0,700;1,400;1,700&display=swap" rel="stylesheet">
<style>
  :root {
    --page: #ffffff;
    --card: #ffffff;
    --amber: #cc7a00;
    --amber-light: #f2bd00;
    --amber-soft: #f39a3a;
    --rust: #c23c0a;
    --oxblood: #8a2a0a;
    --ink-1: #20282e;
    --ink-2: #34444c;
    --ink-3: #4f5c63;
    --ink-4: #6e6e6e;
    --ink-5: #9a9a9a;
    --name: #111111;
    --shadow: rgba(0, 0, 0, 0.28);
  }
  * { margin: 0; padding: 0; box-sizing: border-box; }
  html, body {
    width: 1200px;
    height: 1000px;
    overflow: hidden;
    background: var(--page);
  }
  .canvas {
    position: relative;
    width: 1200px;
    height: 1000px;
  }
  .card {
    position: absolute;
    top: 266px;
    width: 267px;
    height: 467px;
    background: var(--card);
    box-shadow: 4px 5px 8px var(--shadow);
    overflow: hidden;
  }
  .card--front { left: 289px; }
  .card--back { left: 644px; }

  .facet-strip {
    position: absolute;
    left: 53px;
    top: 0;
    width: 161px;
    height: 20px;
    background: linear-gradient(90deg, var(--oxblood) 0%, var(--amber) 8%, var(--amber) 68%, #ff8000 72%, #ff8000 100%);
  }

  .tagline {
    position: absolute;
    left: 49px;
    top: 306px;
    font-family: "PT Sans", sans-serif;
    font-style: italic;
    font-weight: 700;
    font-size: 31px;
    line-height: 26px;
    letter-spacing: -0.6px;
  }
  .tagline span { display: block; }
  .tagline .l1 { color: var(--ink-1); }
  .tagline .l2 { color: var(--ink-2); }
  .tagline .l3 { color: var(--ink-3); }
  .tagline .l4 { color: var(--ink-4); }
  .tagline .l5 { color: var(--ink-5); }

  .facet-panel {
    position: absolute;
    left: 53px;
    top: 0;
    width: 161px;
    height: 338px;
    background:
      linear-gradient(180deg, rgba(242,189,0,0.9) 0%, rgba(204,122,0,0) 30%),
      linear-gradient(160deg, var(--amber-light) 0%, var(--amber) 25%, var(--amber-soft) 45%, #e8730f 65%, var(--rust) 85%, var(--oxblood) 100%);
  }

  .identity {
    position: absolute;
    left: 0;
    width: 100%;
    top: 349px;
    text-align: center;
    font-family: "PT Sans", sans-serif;
  }
  .identity__name {
    font-weight: 700;
    font-size: 21px;
    line-height: 26px;
    color: var(--name);
  }
  .identity__role {
    font-style: italic;
    font-size: 16px;
    line-height: 20px;
    color: var(--name);
  }

  .contact {
    position: absolute;
    left: 50px;
    top: 418px;
    display: flex;
    align-items: center;
    gap: 6px;
    font-family: "PT Sans", sans-serif;
    font-style: italic;
    font-size: 16px;
    color: var(--name);
  }
  .contact__icon { width: 18px; height: 26px; }
</style>
</head>
<body>
<main class="canvas">
  <section class="card card--front" aria-label="Card front">
    <div class="facet-strip" role="img" aria-label="Geometric faceted amber pattern band"></div>
    <p class="tagline">
      <span class="l1">Talent</span>
      <span class="l2">Strategies</span>
      <span class="l3">That</span>
      <span class="l4">Drive</span>
      <span class="l5">Results</span>
    </p>
  </section>

  <section class="card card--back" aria-label="Card back">
    <div class="facet-panel" role="img" aria-label="Geometric faceted pattern in amber, orange and rust tones"></div>
    <div class="identity">
      <p class="identity__name">Rel T</p>
      <p class="identity__role">Art Director</p>
    </div>
    <p class="contact">
      <svg class="contact__icon" viewBox="0 0 18 26" aria-hidden="true">
        <path fill="var(--amber)" d="M5 2 L8 1 L10 7 L7 9 C6.5 12 8 17 11 19 L13 17 L17 21 L15 24 C8 25 2 16 2 8 C2 5 3 3 5 2 Z"/>
      </svg>
      <span class="contact__phone">+1 555 374 9281</span>
    </p>
  </section>
</main>
</body>
</html>
```